Business Card Upgrade

I have designed our business card using our new logo. I think it needs imporovements. We used to have two cards for our business. One card was for our software business, and the other was for our consulting business. We are now in the process of combining our websites, marketing, name, and a new logo.

Our goal is to have a really sharp professional logo. One reason I designed the card the way I did was that our Titles are sometimes long, and by separating the person's name and title, it shows up very well and the title can be adjusted no matter how long it is. Sometimes the title can be 4 or 5 words or more.

We really like our logo on black as it shows up very nice. Our PMS colors are as follows: 368C and 459C.

The Designer that will be working with us will need to deliver the following:

The front and back of the Business Card Design will need to be delivered in a high quality JPEG, and
The front and back of the Business Card Design in Illustrator Format .ai
Any fonts will need to be sent to us if they are not standard and are required to open the Illustrator file correctly.

To help us get a good idea of the card with a title, please use the title: " Director of Software Development "

NOTE: The chosen designer will be selected to design our new letterhead within 2 weeks from the closing of this contest.
Updates

To help us make sure the card design works with longer titles, please use the followign job title on the card:  

"Director of Software and Product Development"

 

ALL DESIGNERS:

1. I appreciate the different angles you are showing the cards, but please be sure and always show the direct view, so I can see the layout and what the person I hand the card will see.

2. Please do not use white.  Please use off white as I don't care for white cards and they get dirty easy and do not represent the designs well.

Dear Designers,

Please provide samples straight one as a viewer of the card will see.  Some of the angles that are presented make it impossible to tell how everything fits, and sometimes even makes areas look skewed. So, please provide a straight sample view.

Target Market(s)

Keystone 400 company executives such as Vice Presidents, and Directors

Industry/Entity Type

Software

Requirements
Must have
• Professional looking Card.

Our customers are Directors, Vice Presidents, and Presidents of companies as large as Keystone 400 companies. The card needs to get attention wile still looking professional.

Delivery of the finished product in Illustrator Format with any fonts needed to edit the text or open the file.

The card will be a heavy stock with a soft touch coating for that silk feel.

```html
<!DOCTYPE html>
<html lang="en">
<head>
<meta charset="utf-8">
<title>Harborline Trade – Business Card</title>
<link rel="stylesheet" href="https://fonts.googleapis.com/css2?family=Open+Sans:wght@400;600;700&family=Montserrat:wght@600&display=swap">
<style>
  :root {
    --page: #d9d6d0;
    --card-front: #f3f2ee;
    --card-back: #121212;
    --brand-green: #6cb33f;
    --brand-gold: #c9a53c;
    --map-tint: #e7e3d2;
    --divider: #dcd9d1;
  }
  * { box-sizing: border-box; margin: 0; padding: 0; }
  html, body {
    width: 1200px; height: 841px; overflow: hidden;
    background: var(--page);
    font-family: "Open Sans", Arial, sans-serif;
  }
  .sheet {
    width: 1200px; height: 841px;
    display: flex; align-items: center; justify-content: center; gap: 40px;
  }
  .card {
    position: relative;
    width: 540px; height: 309px;
    overflow: hidden;
    box-shadow: 0 6px 18px rgba(0,0,0,.18);
  }

  /* Front */
  .card--front { background: var(--card-front); }
  .world-map {
    position: absolute; left: 40px; top: 30px; width: 460px; height: 240px;
    background: radial-gradient(ellipse at 50% 50%, var(--map-tint) 0%, rgba(231,227,210,0) 70%);
  }
  .name-block { position: absolute; left: 0; top: 100px; }
  .name-marker {
    position: absolute; left: 0; top: 6px; width: 26px; height: 28px;
    background: var(--brand-green);
  }
  .person-name {
    position: absolute; left: 32px; top: 0; white-space: nowrap;
    font-weight: 700; font-size: 33px; letter-spacing: -.5px;
    color: var(--brand-green);
  }
  .person-title {
    position: absolute; left: 20px; top: 44px; white-space: nowrap;
    font-weight: 600; font-size: 12.5px;
    color: var(--brand-gold);
  }
  .column-divider {
    position: absolute; left: 300px; top: 60px; width: 2px; height: 200px;
    background: linear-gradient(to bottom, rgba(220,217,209,0), var(--divider), rgba(220,217,209,0));
  }
  .contact-list { position: absolute; left: 318px; top: 100px; list-style: none; }
  .contact-item {
    display: flex; align-items: flex-start; gap: 10px;
    font-weight: 600; font-size: 12.5px; line-height: 1.35;
    color: var(--brand-green); margin-bottom: 22px;
  }
  .contact-icon { width: 14px; height: 14px; flex: none; margin-top: 1px; }

  /* Back */
  .card--back {
    background: var(--card-back);
    display: flex; flex-direction: column; align-items: center; justify-content: center; gap: 18px;
  }
  .brand-name {
    font-family: "Montserrat", Arial, sans-serif; font-weight: 600;
    font-size: 34px; letter-spacing: 4px; color: var(--brand-green);
  }
  .brand-web {
    font-family: "Montserrat", Arial, sans-serif; font-weight: 600;
    font-size: 10px; letter-spacing: 4px; color: var(--brand-green);
  }
</style>
</head>
<body>
<main class="sheet">
  <section class="card card--front" aria-label="Card front">
    <div class="world-map" role="img" aria-label="Faint dotted world map background"></div>
    <div class="name-block">
      <span class="name-marker"></span>
      <h1 class="person-name">DORIAN HALE</h1>
      <p class="person-title">Director of Software and Product Development</p>
    </div>
    <div class="column-divider"></div>
    <ul class="contact-list">
      <li class="contact-item">
        <svg class="contact-icon" viewBox="0 0 14 14"><path d="M1 7 L7 2 L13 7 M3 6 V12 H11 V6" fill="none" stroke="var(--brand-gold)" stroke-width="1.6"/></svg>
        <span>418 Cedar Point Lane<br>AL 36610</span>
      </li>
      <li class="contact-item">
        <svg class="contact-icon" viewBox="0 0 14 14"><rect x="4" y="1" width="6" height="12" rx="1" fill="none" stroke="var(--brand-gold)" stroke-width="1.6"/><line x1="6" y1="11" x2="8" y2="11" stroke="var(--brand-gold)" stroke-width="1.4"/></svg>
        <span>251-555-0148</span>
      </li>
      <li class="contact-item">
        <svg class="contact-icon" viewBox="0 0 14 14"><circle cx="7" cy="7" r="5.8" fill="none" stroke="var(--brand-gold)" stroke-width="1.4"/><ellipse cx="7" cy="7" rx="2.5" ry="5.8" fill="none" stroke="var(--brand-gold)" stroke-width="1.1"/><line x1="1.2" y1="7" x2="12.8" y2="7" stroke="var(--brand-gold)" stroke-width="1.1"/></svg>
        <span>dorianhale@harborline.com<br>www.harborline.com</span>
      </li>
    </ul>
  </section>

  <section class="card card--back" aria-label="Card back">
    <p class="brand-name">HARBORLINE TRADE</p>
    <p class="brand-web">www.harborline.com</p>
  </section>
</main>
</body>
</html>
```